Bright LumaTrex & Equipments

I need to create full stationery design for the company; Business Card, Envelop, Letterheads, Calendar and email template.

Our company is specialized in the import and export of nutritional, pharmaceutical and cosmetics in addition to medical equipments.

These is no limitation on how to use colors within the design.

Target Market(s)

Global

Industry/Entity Type

Healthcare

Other font styles liked:
• a font close to logo. Letterhead body text to be different than the address text

Requirements
Nice to have
• We will have multiple locations so it is good to keep space for future addresses.
• Stationary requirements:
• Letterhead: A4
• Envelopes: 3 regular sizes : large, medium and small (i do not know the sizes)
• Colors: extracted from the logo

```html
<!DOCTYPE html>
<html lang="en">
<head>
<meta charset="utf-8">
<title>Bright LumaTrex &amp; Equipments — Business Card</title>
<link rel="stylesheet" href="https://fonts.googleapis.com/css2?family=Open+Sans:wght@400;600;700&display=swap">
<style>
  :root {
    --sky: #29a6e0;
    --navy: #0d1160;
    --white: #ffffff;
    --backdrop: #e9e6e1;
    --ink-soft: #1b1f6a;
  }
  * { box-sizing: border-box; margin: 0; padding: 0; }
  html, body { width: 1200px; height: 843px; overflow: hidden; }
  body {
    background: var(--backdrop);
    font-family: "Open Sans", Arial, sans-serif;
    display: flex;
    align-items: center;
    justify-content: center;
    gap: 40px;
  }
  .card {
    position: relative;
    width: 540px;
    height: 309px;
    border-radius: 14px;
    overflow: hidden;
    box-shadow: 0 10px 26px rgba(0,0,0,0.18);
  }
  /* Front */
  .card-front {
    background: var(--white);
    display: flex;
    align-items: center;
    justify-content: center;
  }
  .brand {
    display: flex;
    align-items: center;
    gap: 14px;
  }
  .brand-square {
    width: 30px;
    height: 30px;
    background: var(--navy);
    border-radius: 4px;
    flex: none;
  }
  .brand-name {
    color: var(--navy);
    font-weight: 700;
    font-size: 27px;
    letter-spacing: 0.2px;
    line-height: 1.15;
  }
  /* Back */
  .card-back { background: var(--sky); color: var(--white); }
  .back-panel {
    position: absolute;
    left: 236px;
    top: 118px;
    width: 340px;
    height: 230px;
    background: var(--navy);
    border-top-left-radius: 46px;
  }
  .contact {
    position: absolute;
    left: 32px;
    top: 26px;
  }
  .person-name { font-size: 22px; font-weight: 700; line-height: 1.2; }
  .person-role { font-size: 13px; font-weight: 400; margin-bottom: 20px; }
  .address { font-size: 13.5px; line-height: 1.35; margin-bottom: 6px; }
  .contact-list { list-style: none; font-size: 13.5px; line-height: 1.35; }
  .contact-list li { display: flex; align-items: center; gap: 8px; }
  .contact-list svg { width: 12px; height: 12px; flex: none; fill: var(--white); }
</style>
</head>
<body>
  <section class="card card-front" aria-label="Business card front">
    <div class="brand">
      <span class="brand-square"></span>
      <span class="brand-name">Bright LumaTrex &amp; Equipments</span>
    </div>
  </section>

  <section class="card card-back" aria-label="Business card back">
    <div class="back-panel"></div>
    <div class="contact">
      <p class="person-name">Daniel Reyes</p>
      <p class="person-role">CEO/Founder</p>
      <p class="address">4120 Harbor View Road<br>Juneau, Alaska 99801<br>2276 Linden Court<br>Glen Cove, NY 11542</p>
      <ul class="contact-list">
        <li>
          <svg viewBox="0 0 12 12" aria-hidden="true"><path d="M2.5 0.5 L4.5 0.5 L5 3.3 L3.8 4.3 C4.5 5.8 6.2 7.5 7.7 8.2 L8.7 7 L11.5 7.5 L11.5 9.5 C11.5 10.6 10.6 11.5 9.5 11.5 C4.5 11.5 0.5 7.5 0.5 2.5 C0.5 1.4 1.4 0.5 2.5 0.5 Z"/></svg>
          614 522 3091
        </li>
        <li>
          <svg viewBox="0 0 12 12" aria-hidden="true"><rect x="3" y="0.5" width="6" height="3"/><rect x="0.5" y="4" width="11" height="5" rx="1"/><rect x="3" y="8" width="6" height="3.5"/></svg>
          417 230 8865
        </li>
        <li>
          <svg viewBox="0 0 12 12" aria-hidden="true"><path d="M0.5 2 H11.5 V10 H0.5 Z M1.5 3 L6 6.5 L10.5 3 Z" fill-rule="evenodd"/></svg>
          hello@brightlumatrex.com
        </li>
        <li>
          <svg viewBox="0 0 12 12" aria-hidden="true"><circle cx="6" cy="6" r="5.5"/></svg>
          www.brightlumatrex.com
        </li>
      </ul>
    </div>
  </section>
</body>
</html>
```